Lionel Arbusto and Dwight Halvorsen Advertisement

We would like an ad that conveys understated elegance. We are a company that purchases estate jewelry watches and diamonds. We care to a wealthy, upscale clientele.

Target Market(s)

Wealthy upscale.

Industry/Entity Type

It Company

Requirements
Must have
• Elegant Design. Crisp Clean. Attached a doc of how the ad should be arranged.

```html
<!DOCTYPE html>
<html lang="en">
<head>
<meta charset="utf-8">
<title>Lionel Arbusto &amp; Dwight Halvorsen – Ready To Sell?</title>
<link href="https://fonts.googleapis.com/css2?family=Oswald:wght@700&family=Libre+Baskerville:wght@700&family=Tinos:wght@400;700&display=swap" rel="stylesheet">
<style>
  :root {
    --brand-red: #c1272d;
    --ink: #111111;
    --muted: #555555;
    --paper: #ffffff;
    --stone: #e6e6e6;
    --stone-deep: #cfcfcf;
    --backdrop: #ecebe8;
  }
  * { box-sizing: border-box; margin: 0; padding: 0; }
  html, body {
    width: 1200px;
    height: 553px;
    overflow: hidden;
    background: var(--backdrop);
  }
  .ad {
    position: absolute;
    left: 429px;
    top: 0;
    width: 342px;
    height: 553px;
    background: var(--paper);
    overflow: hidden;
  }
  .ad__stage {
    position: absolute;
    left: 42px;
    top: 78px;
    width: 300px;
    height: 259px;
    background: linear-gradient(180deg, var(--stone) 0%, #f1f1f1 100%);
    border-top-left-radius: 150px 120px;
  }
  .ad__gem {
    position: absolute;
    left: 185px;
    top: 139px;
    width: 138px;
    height: 138px;
    border-radius: 12px;
    background: radial-gradient(circle at 45% 40%, #ffffff 0%, #d9d9d9 55%, #a9a9a9 100%);
  }
  .ad__headline {
    position: absolute;
    left: 14px;
    top: 2px;
    font-family: "Oswald", "Arial Narrow", sans-serif;
    font-weight: 700;
    font-size: 76px;
    line-height: 80px;
    color: var(--brand-red);
    letter-spacing: 0.5px;
  }
  .ad__pitch {
    position: absolute;
    left: 0;
    top: 340px;
    width: 342px;
    padding-left: 12px;
    text-align: center;
  }
  .ad__pitch-main {
    font-family: "Libre Baskerville", "Times New Roman", serif;
    font-weight: 700;
    font-size: 26px;
    line-height: 32px;
    color: var(--brand-red);
  }
  .ad__pitch-sub {
    font-family: "Tinos", "Times New Roman", serif;
    font-size: 19px;
    line-height: 20px;
    color: var(--ink);
  }
  .ad__brand {
    position: absolute;
    left: 0;
    top: 403px;
    width: 342px;
    padding-left: 12px;
    text-align: center;
    font-family: "Tinos", "Times New Roman", serif;
    font-size: 12px;
    letter-spacing: 1.5px;
    text-transform: uppercase;
    color: var(--muted);
  }
  .ad__venue {
    position: absolute;
    left: 14px;
    top: 441px;
    font-family: "Tinos", "Times New Roman", serif;
    font-size: 18px;
    color: var(--ink);
  }
  .ad__partners {
    position: absolute;
    right: 12px;
    top: 437px;
    text-align: right;
    font-family: "Tinos", "Times New Roman", serif;
    font-size: 11px;
    line-height: 13px;
    font-variant: small-caps;
    letter-spacing: 0.6px;
    color: var(--muted);
  }
  .ad__contacts {
    position: absolute;
    left: 14px;
    top: 469px;
    list-style: none;
    font-family: "Tinos", "Times New Roman", serif;
    font-size: 13px;
    line-height: 17px;
    color: var(--ink);
  }
  .ad__contacts li {
    display: flex;
    align-items: center;
    gap: 7px;
  }
  .ad__contacts svg {
    width: 11px;
    height: 11px;
    fill: var(--brand-red);
    flex: none;
  }
  .ad__band {
    position: absolute;
    left: 0;
    bottom: 0;
    width: 342px;
    height: 33px;
    background: var(--brand-red);
    color: var(--paper);
    font-family: "Tinos", "Times New Roman", serif;
    font-weight: 700;
    font-size: 14px;
    line-height: 33px;
    text-align: center;
  }
</style>
</head>
<body>
  <article class="ad">
    <div class="ad__stage"></div>
    <div class="ad__gem" role="img" aria-label="Photograph of an emerald-cut diamond"></div>
    <h1 class="ad__headline">Ready To<br>Sell?</h1>

    <div class="ad__pitch">
      <p class="ad__pitch-main">Utmost Discretion</p>
      <p class="ad__pitch-sub">By Appointment</p>
    </div>

    <p class="ad__brand">Arbusto &amp; Halvorsen</p>

    <p class="ad__venue">Via Serenata</p>
    <p class="ad__partners">Lionel Arbusto &amp;<br>Dwight Halvorsen</p>

    <ul class="ad__contacts">
      <li>
        <svg viewBox="0 0 12 12" aria-hidden="true"><path d="M6 0.5 0 6h1.8v5.5h3V8h2.4v3.5h3V6H12z"/></svg>
        118-B Laurel Avenue Palm Harbor, FL 33490
      </li>
      <li>
        <svg viewBox="0 0 12 12" aria-hidden="true"><path d="M0 2h12v1.2L6 7 0 3.2z M0 4.6 6 8.4l6-3.8V10H0z"/></svg>
        support@arbustohalvorsen.com
      </li>
      <li>
        <svg viewBox="0 0 12 12" aria-hidden="true"><path d="M2.4 0.6 4.6 3 3.4 4.6c.8 1.7 2.2 3.1 3.9 3.9L8.9 7.3l2.5 2.3-1.3 1.8C5.2 11.3.7 6.8.6 1.9z"/></svg>
        555.014.2290
      </li>
    </ul>

    <div class="ad__band">support@arbustohalvorsen.com</div>
  </article>
</body>
</html>
```